Postcard for Dental Lab to Dental Lab

We are a wholesale Outsourcing Dental Lab. We are looking for a postcard design that will attract new customers and accounts. We market to Only other dental Labs. We are looking for a design based around "new year resolutions list for a dental lab" Our logo colors are green, gold and white. We want a box with a check mark in it showing that our lab has meet all of the new year resolution lists.

We are looking for a new years resolutions postcard. It should have a professional look as we are sending it to dental Labs.

Maybe something that shows a fresh start and new year. The main focus point would be a "New years resolution" List. This list should look like it has been written on paper. It should list things like
The heading should read. "New Years Resolutions list"
1. Work less Hours while maintaining current income
2. Expand current dental Lab
3. Make More money with Less headaches.
4. Gain more freedom from long hours behind bench.

Then another heading: "Ways to achieve resolutions list"
"Find outsourcing dental lab that offers..."

1. Find a experienced full service dental Lab

2. Lab that is FDA and KTRC certified.

3. Competitive prices.

4. Has consistent quality restorations and products.

5. BRIVEN WORKS
That was easy.

On the back of the card we would like some bullet points.
1. ISO 9001, 13485 and FDA Certified.
2. Restorative Goods Quality Review Scheme (RGQRS) certified.
3. 5 year warranty on fixed and 2 years on removable.
4. Local Customer service in Phoenix Arizona assigned to your office and cases.
5. Higher productivity- Allows you to provide more units from your lab with the same number of technicians.

Here are two customer quotes that we can use.
"Impressive work....Better than what we can do locally!..."

"Thanks for your wonderful service, our business is increasing by 20% per month..."

Please have and area for the mailing address and return address. We are looking for a headline that is large on the front of the post card that will grab attention. Maybe an image of sparklers or fireworks or something with a new years new start.
Keep the designs coming as we are really needing to get this design finished quick.
Thanks!

I have uploaded a sample of what we are looking for. This is from a diffrent dental lab but with the same idea. Please look at this design but include what we have asked for. thank you
Updates

This flyer will be 6” x 11” with an eye catching basic design on the front and some more detailed info on the back.  I would like to focus on getting a great front design and then we can work on making the back coordinate.  Can have some brighter colors for the “New Year’s Resolution” part (look festive and eye catching) Maybe some Fireworks in the background

This flyer will be an introduction to our business in new areas that we have not worked in before. 
The concept is to introduce our lab, let them know we will be offering our services in their regions and do it in a creative, eye catching way. 

The concept I would like for the flyer is a new year’s resolution list that has a list of things they need to complete their goals.  The list is needs to look like a piece of paper with a visually appealing header of “NEW YEAR’S RESOLUTION” and a hand written look of the rest of what is below. The bullet points need to be boxes and they need check marks in them like they put a check mark in the boxes by hand.

On the front of the postcard there needs to be a place for our phone number 855-314-9087 and then an area to place "Special Trial offer" 5 free PFM'S!

Reason: I would like to provide more feed back. Due to the holiday we will be extending the deadline. Thank you for the designs please keep them coming.

Reason: Still looking for a good design. please keep them coming. Thank you

Target Market(s)

Dental LAB OWNERS.

Industry/Entity Type

Dental

Requirements
Must have
• New Year resolutions theme. Looking for a list that is written on a piece of paper with checkboxes next to every one of the lists.

```html
<!DOCTYPE html>
<html lang="en">
<head>
<meta charset="utf-8">
<title>Briven Works – New Year's Resolutions Postcard</title>
<link href="https://fonts.googleapis.com/css2?family=Oswald:wght@600&family=Shadows+Into+Light+Two&family=Open+Sans:wght@700;800&display=swap" rel="stylesheet">
<style>
  :root {
    --night: #050505;
    --paper: #ffffff;
    --rule: #b9b9b9;
    --ink: #1c1c1c;
    --brand-green: #4d6b58;
    --offer-yellow: #fff200;
    --offer-green: #1f4d2c;
    --note-yellow: #f6f0b4;
    --note-edge: #e6dd95;
    --white: #ffffff;
  }
  * { margin: 0; padding: 0; box-sizing: border-box; }
  html, body { width: 1200px; height: 655px; overflow: hidden; background: #ffffff; }
  .postcard {
    position: relative;
    width: 1200px;
    height: 655px;
    overflow: hidden;
    background: var(--paper);
    font-family: "Shadows Into Light Two", cursive;
    color: var(--ink);
  }
  .sky {
    position: absolute; left: 0; top: 0; width: 1200px; height: 197px;
    background:
      radial-gradient(circle at 7% 30%, rgba(225,60,150,.55), transparent 8%),
      radial-gradient(circle at 24% 20%, rgba(240,110,30,.55), transparent 8%),
      radial-gradient(circle at 40% 14%, rgba(230,225,60,.55), transparent 9%),
      radial-gradient(circle at 57% 30%, rgba(240,180,40,.45), transparent 6%),
      radial-gradient(circle at 76% 16%, rgba(230,60,60,.55), transparent 9%),
      radial-gradient(circle at 93% 28%, rgba(240,200,80,.55), transparent 10%),
      var(--night);
  }
  .headline {
    position: absolute; left: 42px; top: 87px;
    font-family: "Oswald", sans-serif; font-weight: 600;
    font-size: 88px; line-height: 1; letter-spacing: -1.5px;
    color: var(--white); white-space: nowrap;
  }
  .resolutions { position: absolute; left: 0; top: 197px; width: 1200px; list-style: none; }
  .resolution {
    height: 59px;
    border-bottom: 2px solid var(--rule);
    display: flex; align-items: center;
    padding-left: 44px;
    font-size: 22px;
  }
  .resolution:first-child { height: 76px; padding-top: 18px; }
  .resolution .tick { width: 46px; height: 46px; margin-right: 16px; flex: none; }
  .brand-name {
    position: absolute; left: 50px; top: 506px;
    font-size: 32px; color: var(--brand-green);
  }
  .phone-band {
    position: absolute; left: 0; top: 568px; width: 1200px; height: 87px;
    background: var(--night);
  }
  .phone {
    position: absolute; left: 52px; top: 578px;
    font-family: "Open Sans", sans-serif; font-weight: 700;
    font-size: 45px; color: var(--white); letter-spacing: .5px;
  }
  .offer {
    position: absolute; left: 360px; top: 482px;
    width: 280px; height: 98px;
    background: var(--offer-yellow);
    transform: rotate(-13deg);
    color: var(--offer-green);
    font-family: "Open Sans", sans-serif; font-weight: 800;
    text-align: center; white-space: nowrap;
    padding-top: 8px;
    box-shadow: 0 3px 6px rgba(0,0,0,.25);
  }
  .offer-kicker { font-size: 23px; line-height: 1.2; font-weight: 700; }
  .offer-deal { font-size: 36px; line-height: 1.3; }
  .note {
    position: absolute; left: 606px; top: 227px;
    width: 535px; height: 520px;
    background: var(--note-yellow);
    border: 1px solid var(--note-edge);
    transform: rotate(-9deg);
    transform-origin: 0 0;
    box-shadow: 4px 6px 10px rgba(0,0,0,.25);
    padding: 24px 28px 0 26px;
  }
  .note-title {
    font-size: 34px; padding-bottom: 2px;
    border-bottom: 2px solid var(--ink);
    width: 460px; margin-left: 4px;
  }
  .steps { list-style: none; margin-top: 16px; }
  .step {
    display: flex; align-items: center;
    min-height: 64px; font-size: 22px; line-height: 1.25;
  }
  .step .tick { width: 50px; height: 50px; margin-right: 16px; flex: none; }
  .step-brand { font-size: 30px; color: var(--brand-green); letter-spacing: 1px; }
  .step-aside { display: block; font-size: 21px; margin-left: 175px; }
</style>
</head>
<body>
<svg width="0" height="0" style="position:absolute" aria-hidden="true">
  <symbol id="tick" viewBox="0 0 50 50">
    <rect x="3" y="13" width="32" height="32" fill="none" stroke="#1c1c1c" stroke-width="2"/>
    <path d="M10 28 L19 40 C26 26 35 14 48 3" fill="none" stroke="#1c1c1c" stroke-width="2.4" stroke-linecap="round" stroke-linejoin="round"/>
  </symbol>
</svg>

<main class="postcard">
  <div class="sky" role="img" aria-label="Colourful fireworks bursting across a night sky"></div>
  <h1 class="headline">NEW YEAR’S RESOLUTIONS</h1>

  <ul class="resolutions">
    <li class="resolution"><svg class="tick"><use href="#tick"/></svg>Work fewer hours while maintaining current income</li>
    <li class="resolution"><svg class="tick"><use href="#tick"/></svg>Expand current dental lab</li>
    <li class="resolution"><svg class="tick"><use href="#tick"/></svg>Make more money with fewer headaches</li>
    <li class="resolution"><svg class="tick"><use href="#tick"/></svg>Gain more freedom from long hours behind the bench</li>
    <li class="resolution"></li>
  </ul>

  <p class="brand-name">Briven Works</p>

  <div class="phone-band"></div>
  <p class="phone">855-314-9087</p>

  <section class="note">
    <h2 class="note-title">Ways to Achieve Resolutions</h2>
    <ul class="steps">
      <li class="step"><svg class="tick"><use href="#tick"/></svg>Find an experienced full service dental lab</li>
      <li class="step"><svg class="tick"><use href="#tick"/></svg>Lab must be FDA and KTRC certified</li>
      <li class="step"><svg class="tick"><use href="#tick"/></svg>Competitive prices</li>
      <li class="step"><svg class="tick"><use href="#tick"/></svg>Has consistent quality restorations<br>and products</li>
      <li class="step"><svg class="tick"><use href="#tick"/></svg><span><span class="step-brand">BRIVEN WORKS</span><span class="step-aside">That was easy!</span></span></li>
    </ul>
  </section>

  <div class="offer">
    <p class="offer-kicker">Special Trial Offer</p>
    <p class="offer-deal">5 Free PFMs!</p>
  </div>
</main>
</body>
</html>
```